We need a Word Template for Custom Laboratory Results from an independent laboratory

The test is a novel biomarker for a chronic pain condition called endometriosis. It is expressed as a percentage. We will upload a sample result. We are looking for improved graphic fidelity with more attention to design and spacing. Emphasis should be placed on the overall result, i.e. the patient percentage results. Considerationis going to be given to the most appealing graphic result.

Target Market(s)

Women aged 19-45

Colors
0054AA
0677BA
7BADD7
CADEEF
E8F1F8

```html
<!DOCTYPE html>
<html lang="en">
<head>
<meta charset="utf-8">
<title>EndoSense Micro-RNA Endometriosis Assay – Your Results</title>
<link href="https://fonts.googleapis.com/css2?family=Oswald:wght@400;500&family=Open+Sans:wght@400;600;700&display=swap" rel="stylesheet">
<style>
  :root {
    --canvas: #f1f5f8;
    --white: #ffffff;
    --teal-light: #4fbfc7;
    --teal: #1fa0ad;
    --teal-deep: #0d8797;
    --teal-ink: #0b5d69;
    --royal: #3a56ad;
    --blue: #0054aa;
    --blue-mid: #0677ba;
    --sky: #7badd7;
    --mist: #cadeef;
    --mist-pale: #e8f1f8;
    --panel-grey: #e4eaec;
    --text-grey: #4a4f55;
    --field: #f4f8fb;
  }
  * { box-sizing: border-box; margin: 0; padding: 0; }
  html, body { width: 1200px; height: 1200px; overflow: hidden; }
  body { background: var(--canvas); font-family: "Open Sans", Arial, sans-serif; position: relative; }

  .results-sheet {
    position: absolute; left: 257px; top: 98px;
    width: 720px; height: 1017px;
    overflow: hidden;
    box-shadow: 0 4px 18px rgba(20, 60, 90, 0.14);
    background: var(--teal);
  }
  .sheet-shapes { position: absolute; inset: 0; }

  .brand-block { position: absolute; left: 40px; top: 30px; width: 300px; display: flex; flex-direction: column; gap: 6px; }
  .brand-row { display: flex; align-items: center; gap: 12px; }
  .brand-dot { flex: none; width: 56px; height: 56px; border-radius: 50%; background: var(--sky); }
  .brand-name { font-family: "Open Sans", Arial, sans-serif; font-weight: 600; color: var(--royal); font-size: 24px; line-height: 1.15; }
  .brand-partner { margin-left: 100px; }

  .assay-title {
    position: absolute; left: 31px; top: 246px;
    font-family: "Oswald", "Arial Narrow", sans-serif; font-weight: 400;
    font-size: 45px; line-height: 1.03; color: var(--white); letter-spacing: 0.2px;
  }
  .results-bar {
    position: absolute; left: 31px; top: 357px; width: 383px; height: 49px;
    background: var(--royal); color: var(--white);
    font-family: "Oswald", "Arial Narrow", sans-serif; font-size: 27px; letter-spacing: 3.5px;
    display: flex; align-items: center; justify-content: center;
  }

  .patient-fields { position: absolute; left: 33px; top: 425px; width: 654px;
    display: grid; grid-template-columns: 320px 320px; column-gap: 14px; row-gap: 22px; }
  .field-label { display: block; color: var(--white); font-weight: 600; font-size: 17px; margin-bottom: 6px; letter-spacing: 0.2px; }
  .field-box { height: 36px; background: var(--field); border-radius: 2px; }

  .score-badge {
    position: absolute; left: 73px; top: 628px; width: 184px; height: 184px;
    border-radius: 50%; background: var(--white);
    box-shadow: 0 2px 10px rgba(0,0,0,0.15);
    display: flex; align-items: center; justify-content: center;
  }
  .score-core {
    width: 160px; height: 160px; border-radius: 50%;
    background: radial-gradient(circle, #8fb4ea 0%, #4b73d2 45%, #2c4fb1 100%);
    display: flex; align-items: center; justify-content: center;
    color: var(--white); font-family: "Oswald", "Arial Narrow", sans-serif; font-weight: 500;
    font-size: 52px; letter-spacing: -1px;
  }
  .score-core .pct { font-size: 38px; }

  .score-caption {
    position: absolute; left: 294px; top: 713px; width: 340px;
    color: var(--teal-ink); font-weight: 700; font-size: 17px; line-height: 1.3;
  }
  .score-caption .control { color: var(--royal); display: block; }

  .range-pill {
    position: absolute; left: 263px; top: 822px; width: 327px; height: 36px;
    border-radius: 0 18px 18px 0;
    background: linear-gradient(90deg, #6fd0d3 0%, var(--teal) 45%, var(--royal) 100%);
    color: var(--white); font-weight: 600; font-size: 18px; letter-spacing: 5px;
    display: flex; align-items: center; justify-content: center;
  }

  .range-table { position: absolute; left: 129px; top: 870px; width: 461px; border-collapse: collapse; }
  .range-table td { height: 29.5px; border-bottom: 1px solid var(--teal); font-size: 16.5px; vertical-align: middle; padding-top: 2px; }
  .range-table .range-value { color: var(--teal-deep); font-weight: 600; padding-left: 12px; width: 164px; }
  .range-table .range-meaning { color: var(--text-grey); }

  .footer-band { position: absolute; left: 0; bottom: 0; width: 100%; height: 18px; background: var(--royal); }
</style>
</head>
<body>
  <main class="results-sheet">
    <svg class="sheet-shapes" width="720" height="1017" viewBox="0 0 720 1017">
      <defs>
        <linearGradient id="tealWash" x1="0" y1="0" x2="0" y2="1">
          <stop offset="0" stop-color="#5cc7cd"/>
          <stop offset="0.45" stop-color="#2aa6b2"/>
          <stop offset="0.75" stop-color="#0f8a9a"/>
        </linearGradient>
        <linearGradient id="photoTone" x1="0" y1="0" x2="1" y2="1">
          <stop offset="0" stop-color="#d9d3cc"/>
          <stop offset="0.55" stop-color="#b9cfd6"/>
          <stop offset="1" stop-color="#9fbfcc"/>
        </linearGradient>
      </defs>
      <rect width="720" height="1017" fill="url(#tealWash)"/>
      <path d="M0,0 H405 C360,120 230,178 0,150 Z" fill="#ffffff"/>
      <path d="M0,770 C170,690 420,620 720,655" fill="none" stroke="#6fcfd4" stroke-width="3"/>
      <path d="M0,750 C180,680 430,630 720,650 V1017 H0 Z" fill="var(--panel-grey)"/>
      <path d="M272,700 C420,650 560,640 720,655 V1017 H272 Z" fill="#ffffff"/>
      <rect x="266" y="690" width="8" height="327" fill="#d3dcdf"/>
      <path d="M380,0 H720 V306 C610,336 470,300 405,190 C372,130 368,50 380,0 Z" fill="url(#photoTone)" stroke="#ffffff" stroke-width="10" role="img" aria-label="Photograph of a woman in a light blue dress with a hand on her abdomen, glowing uterus illustration overlaid"/>
    </svg>

    <div class="brand-block">
      <div class="brand-row">
        <span class="brand-dot"></span>
        <span class="brand-name">Meridian<br>Fertility Centre</span>
      </div>
      <span class="brand-name brand-partner">Novalis Labs</span>
    </div>

    <h1 class="assay-title">ENDOSENSE MICRO-RNA<br>ENDOMETRIOSIS ASSAY</h1>
    <div class="results-bar">YOUR RESULTS</div>

    <section class="patient-fields">
      <div><span class="field-label">FIRST NAME</span><div class="field-box"></div></div>
      <div><span class="field-label">LAST NAME</span><div class="field-box"></div></div>
      <div><span class="field-label">HEALTH CARD NUMBER</span><div class="field-box"></div></div>
      <div><span class="field-label">DATE OF BIRTH</span><div class="field-box"></div></div>
    </section>

    <div class="score-badge"><div class="score-core">38.7<span class="pct">%</span></div></div>

    <p class="score-caption">PREDICTED PROBABILITY OF ENDOMETRIOSIS COMPARED TO SURGICAL CONTROLS <span class="control">(100% PROBABILITY)</span></p>

    <div class="range-pill">REFERENCE RANGE</div>
    <table class="range-table">
      <tr><td class="range-value">0 - 29.9%</td><td class="range-meaning">Low probability of endometriosis</td></tr>
      <tr><td class="range-value">29.9 - 44.9%</td><td class="range-meaning">Inconclusive</td></tr>
      <tr><td class="range-value">45.0 - 55.0%</td><td class="range-meaning">Intermediate risk of endometriosis</td></tr>
      <tr><td class="range-value">65.0 - 99.9%</td><td class="range-meaning">Highly probable endometriosis</td></tr>
    </table>

    <div class="footer-band"></div>
  </main>
</body>
</html>
```